Law firm Seeks Modern and Engaging Site Redesign

Law firm seeks a new web site. Should be modern, but retaining existing logo. Needs to include contact section, professional bio, services offered, and contact information.

The site should be modern, responsive, and able to be SEO optimized.

The finished product should be coded in a Wordpress site, which I will provide. I can work with other platforms, including Wix, but WP is preferred.

Note the current site is https://www.tallowfieldlaw.example/#/home

Target Market(s)

Family Law Practice

Industry/Entity Type

Legal

Coding

Coded - Design and coding required

Number of Pages Required

4 page

Font styles to use
Sans Serif

Requirements
Must have
• Service description
Bio pages for partners
Contact Form
Awards/Publication page

```html
<!DOCTYPE html>
<html lang="en">
<head>
<meta charset="utf-8">
<title>Tallowfield | Marsh — Attorneys at Law</title>
<link href="https://fonts.googleapis.com/css2?family=Lato:wght@300;400;700&family=Spectral:wght@300;400&display=swap" rel="stylesheet">
<style>
:root{
  --blue:#5a78e0;
  --ink:#2b2b2b;
  --text:#555a60;
  --muted:#8a8f96;
  --light:#f4f5f7;
  --badge:#e4e7ee;
  --dark:#2e2f33;
  --white:#ffffff;
}
*{box-sizing:border-box;margin:0;padding:0}
html,body{width:1200px;height:4367px;overflow:hidden}
body{position:relative;font-family:"Lato",sans-serif;color:var(--text);background:var(--white)}
.abs{position:absolute}
.serif{font-family:"Spectral",serif;font-weight:400}
.eyebrow{font-size:10px;letter-spacing:2px;text-transform:uppercase;text-align:center;color:var(--blue)}
.section-title{font-family:"Spectral",serif;font-weight:400;font-size:29px;color:var(--ink);text-align:center}
.btn{display:flex;align-items:center;justify-content:center;background:var(--blue);color:var(--white);font-size:11px;font-weight:700;text-transform:uppercase;letter-spacing:.3px}

/* Hero */
.hero{left:0;top:0;width:1200px;height:675px;background:linear-gradient(100deg,#4a4c50 0%,#8d8f93 45%,#d8d8d8 100%)}
.hero-scene{left:0;top:0;width:1200px;height:675px;background:linear-gradient(90deg,rgba(40,42,46,.75) 0%,rgba(60,62,66,.35) 45%,rgba(255,255,255,0) 100%)}
.hero-people{left:600px;top:85px;width:470px;height:590px;background:linear-gradient(180deg,#9aa0a8 0%,#2d3546 55%,#1d2435 100%);border-radius:200px 200px 0 0;opacity:.85}
.brand{left:160px;top:20px;color:var(--white);font-family:"Spectral",serif}
.brand-name{font-size:21px}
.brand-sub{font-size:8px;margin-left:95px;margin-top:-3px;font-family:"Lato",sans-serif}
.nav{left:425px;top:28px;display:flex;gap:26px;font-size:11px;color:var(--white)}
.nav .active{font-weight:700}
.nav-phone{left:859px;top:19px;width:180px;height:37px;border:1.5px solid rgba(255,255,255,.8);border-radius:3px;color:var(--white);font-size:15px;display:flex;align-items:center;justify-content:center;gap:8px}
.hero-eyebrow{left:163px;top:261px;font-size:9.5px;letter-spacing:1.5px;color:var(--white)}
.hero-title{left:162px;top:286px;font-size:30px;line-height:37px;color:var(--white)}
.hero-btn{left:162px;top:390px;width:172px;height:40px}

/* About */
.about-text{left:228px;top:822px;width:744px;font-size:11px;line-height:19.5px;text-align:center}
.about-text p{margin-bottom:19px}
.team-card{top:1217px;width:150px;height:210px;background:var(--light)}
.team-photo{width:150px;height:150px;background:linear-gradient(160deg,#c9ccd2,#5c6470 60%,#2f3440)}
.team-name{height:60px;display:flex;align-items:center;justify-content:center;text-align:center;color:var(--blue);font-size:13px;line-height:20px;padding:0 12px}

/* Practice */
.practice-band{left:0;top:1502px;width:1200px;height:263px;background:var(--blue)}
.practice-bg{left:0;top:1765px;width:1200px;height:488px;background:var(--light)}
.practice-card{top:1666px;width:314px;height:509px;background:var(--white)}
.practice-photo{width:314px;height:226px}
.practice-body{padding:22px 22px 0}
.practice-body h3{font-family:"Spectral",serif;font-weight:400;font-size:18px;color:var(--ink);margin-bottom:12px}
.practice-body p{font-size:11px;line-height:19px;margin-bottom:12px}
.practice-body ul{list-style:none;font-size:11px}
.practice-body li{position:relative;padding-left:16px;height:26px}
.practice-body li:before{content:"";position:absolute;left:1px;top:5px;width:5px;height:5px;border-radius:50%;background:var(--blue)}
.practice-body .btn{width:110px;height:33px;margin-top:12px;font-size:10px}

/* Testimonials */
.testimonials{left:0;top:2253px;width:1200px;height:412px;background:linear-gradient(180deg,#3a3c40 0%,#2a2c30 100%)}
.avatar{left:268px;top:2402px;width:112px;height:112px;border-radius:50%;background:linear-gradient(150deg,#e9d6c7,#a8765a);border:3px solid rgba(255,255,255,.8)}
.quote-text{left:400px;top:2410px;width:540px;font-size:11px;line-height:20px;color:#e6e6e6}
.quote-name{left:400px;top:2488px;font-family:"Spectral",serif;font-size:14px;color:var(--white)}
.reviews-btn{left:398px;top:2551px;width:180px;height:41px}

/* Awards */
.award{top:2818px;background:var(--badge)}
.award-round{width:92px;height:92px;border-radius:50%}
.award-box{width:148px;height:68px}

/* News */
.news{left:0;top:2983px;width:1200px;height:556px;background:var(--light)}
.news-card{top:3134px;width:270px}
.news-photo{width:270px;height:180px}
.news-date{font-size:9px;color:var(--muted);margin-top:17px}
.news-title{font-size:13.5px;color:var(--ink);margin-top:9px}
.news-text{font-size:10px;line-height:19px;margin-top:6px}
.news-more{font-size:9.5px;font-weight:700;letter-spacing:1.5px;color:var(--blue);margin-top:13px}

/* Contact */
.contact{left:0;top:3539px;width:1200px;height:648px;background:var(--blue)}
.contact-sub{left:270px;top:3668px;width:660px;text-align:center;font-size:11px;line-height:19px;color:var(--white);text-transform:uppercase}
.contact-phone{left:470px;top:3719px;display:flex;align-items:center;gap:14px;color:var(--white);font-family:"Spectral",serif;font-size:29px}
.field{height:37px;border:1px solid rgba(255,255,255,.7);color:var(--white);font-size:10px;padding:11px 8px}
.send-btn{left:161px;top:4056px;width:180px;height:40px;background:var(--white);color:var(--ink);font-size:11px;font-weight:700}
.map{left:612px;top:3800px;width:425px;height:299px;background:linear-gradient(135deg,#eef0ea 0%,#e3e8df 50%,#cfdff0 100%)}

/* Footer */
.footer{left:0;top:4187px;width:1200px;height:180px;background:var(--dark)}
.f-icon{top:4224px;width:60px;height:60px;border-radius:50%;border:1.5px solid #cfd0d3;display:flex;align-items:center;justify-content:center}
.f-label{font-size:9px;letter-spacing:1.5px;color:var(--blue)}
.f-value{font-size:11px;line-height:19px;color:#e3e3e3;margin-top:6px}
.copyright{left:0;top:4335px;width:1200px;text-align:center;font-size:9.5px;color:#9a9ba0}
.copyright span{color:var(--blue)}
</style>
</head>
<body>

<!-- Hero -->
<div class="abs hero" role="img" aria-label="Hand signing a legal document on a desk"></div>
<div class="abs hero-scene"></div>
<div class="abs hero-people" role="img" aria-label="Two partners in dark suits standing side by side"></div>
<div class="abs brand">
  <div class="brand-name">Tallowfield | Marsh</div>
  <div class="brand-sub">Attorneys at Law</div>
</div>
<nav class="abs nav"><span class="active">Home</span><span>About</span><span>Family Law</span><span>Criminal Law</span><span>Contact</span></nav>
<div class="abs nav-phone">
  <svg width="14" height="14" viewBox="0 0 24 24" fill="#fff"><path d="M6.6 10.8c1.4 2.8 3.8 5.1 6.6 6.6l2.2-2.2c.3-.3.7-.4 1-.2 1.1.4 2.3.6 3.6.6.6 0 1 .4 1 1V20c0 .6-.4 1-1 1C10.6 21 3 13.4 3 4c0-.6.4-1 1-1h3.5c.6 0 1 .4 1 1 0 1.3.2 2.5.6 3.6.1.3 0 .7-.2 1l-2.3 2.2z"/></svg>
  (555) 014-2141
</div>
<div class="abs hero-eyebrow">FAMILY AND CRIMINAL LAWYERS IN HARLOW COUNTRY</div>
<h1 class="abs hero-title serif">A Family &amp; Criminal Lawyer<br>who speaks for you.</h1>
<div class="abs btn hero-btn">Contact With Us</div>

<!-- About -->
<div class="abs eyebrow" style="left:0;top:750px;width:1200px">Attorneys at Law</div>
<h2 class="abs section-title" style="left:0;top:764px;width:1200px">About Tallowfield | Marsh</h2>
<div class="abs about-text">
  <p>The law firm of Tallowfield Marsh, LLC is based in Harlow County, conveniently located in Fenmoor, New Jersey in 48 Civic Plaza. We serve the needs of clients throughout Harlow County, as well as, clients from several other counties, including, but not limited to, Ashby, Corran, Delmont and Wexley. Between our partners, we have over 30+ years of experience assisting clients with all of their family law and criminal law needs.</p>
  <p>Often times the areas of family law and criminal law cross paths, which can be both emotionally and financially complex. We understand that our client's case is unique and pride ourselves on being responsive to all of our clients needs.</p>
  <p>Mr. Tallowfield began his career as the law clerk to the Honorable Arthur G. Pennick, J.S.C., retired, the then Presiding Judge of the Criminal Part and thereafter as an Assistant Prosecutor with the Harlow County Prosecutors Office. Mr. Marsh began his career as the law clerk to the Honorable Walter E. Brandt, J.S.C., retired, who oversaw the Court's Juvenile Delinquency docket, the state family services agency docket and all other Family Part matters. As a result of their experience in the court system, Mr. Tallowfield and Mr. Marsh bring a unique perspective to their practice.</p>
  <p>Both Mr. Tallowfield and Mr. Marsh practiced privately for well over a decade as partners in two of Harlow County's most established Family Law firms before joining together to use their knowledge and experience to assist their clients with all of their legal needs.</p>
  <p>Whether your needs are family or criminal law related, contact Tallowfield Marsh, LLC to schedule a consultation.</p>
</div>
<div class="abs team-card" style="left:263px"><div class="team-photo" role="img" aria-label="Portrait of Daniel R. Tallowfield"></div><div class="team-name">Daniel R. Tallowfield</div></div>
<div class="abs team-card" style="left:437px"><div class="team-photo" role="img" aria-label="Portrait of Owen P. Marsh"></div><div class="team-name">Owen P. Marsh</div></div>
<div class="abs team-card" style="left:612px"><div class="team-photo" role="img" aria-label="Portrait of Lena J. Ashcombe"></div><div class="team-name">Lena J. Ashcombe</div></div>
<div class="abs team-card" style="left:787px"><div class="team-photo" role="img" aria-label="Portrait of Maren T. Holloway" style="background:linear-gradient(160deg,#e8eaee,#b8bcc4 60%,#8c919a)"></div><div class="team-name">Maren T.<br>Holloway</div></div>

<!-- Practice areas -->
<div class="abs practice-band"></div>
<div class="abs practice-bg"></div>
<div class="abs eyebrow" style="left:0;top:1586px;width:1200px;color:#fff;font-size:9px">Tallowfield | Marsh</div>
<h2 class="abs section-title" style="left:0;top:1602px;width:1200px;color:#fff">Our Practice Areas</h2>
<div class="abs practice-card" style="left:271px">
  <div class="practice-photo" role="img" aria-label="Parents kissing their baby daughter" style="background:linear-gradient(135deg,#c99a7e,#8a5b6e 55%,#5e4a58)"></div>
  <div class="practice-body">
    <h3>Family Law</h3>
    <p>Our firm accepts all kinds of family law matters,<br>including:</p>
    <ul><li>Divorce</li><li>Child Custody</li><li>Child Support</li><li>Alimony</li></ul>
    <div class="btn">Learn More</div>
  </div>
</div>
<div class="abs practice-card" style="left:615px">
  <div class="practice-photo" role="img" aria-label="Handcuffed hands held open" style="background:linear-gradient(160deg,#6e6e70,#3a3433 55%,#1e1c1c)"></div>
  <div class="practice-body">
    <h3>Criminal Law</h3>
    <p>Our firm accepts all kinds of criminal law matters,<br>including:</p>
    <ul><li>Assault</li><li>Domestic Violence</li><li>Drug Crimes</li><li>DWI/DUI</li></ul>
    <div class="btn">Learn More</div>
  </div>
</div>

<!-- Testimonials -->
<div class="abs testimonials" role="img" aria-label="Dimmed city skyline at dusk"></div>
<div class="abs eyebrow" style="left:0;top:2329px;width:1200px;color:#e0e0e0;font-size:9px">Testimonials</div>
<h2 class="abs section-title" style="left:0;top:2343px;width:1200px;color:#fff">What Our Cliens Say</h2>
<div class="abs avatar" role="img" aria-label="Client portrait"></div>
<p class="abs quote-text">Lorem Ipsum is simply dummy text of the printing and typesetting industry. Lorem Ipsum has been the industry's standard dummy text ever since the 1500s, when an unknown printer took a galley of type and scrambled it to make a type specimen book.</p>
<div class="abs quote-name">– CLIENT NAME</div>
<div class="abs btn reviews-btn">Read More Reviews</div>

<!-- Awards -->
<div class="abs eyebrow" style="left:0;top:2741px;width:1200px;font-size:9px">Tallowfield | Marsh</div>
<h2 class="abs section-title" style="left:0;top:2755px;width:1200px">Our Awards</h2>
<div class="abs award award-round" style="left:337px" role="img" aria-label="Attorney rating award"></div>
<div class="abs award award-box" style="left:525px;top:2830px" role="img" aria-label="Peer recognition award"></div>
<div class="abs award award-round" style="left:764px" role="img" aria-label="Trial lawyers membership award"></div>

<!-- News -->
<div class="abs news"></div>
<h2 class="abs section-title" style="left:0;top:3056px;width:1200px">Latest News</h2>
<div class="abs news-card" style="left:161px">
  <div class="news-photo" role="img" aria-label="Couple sitting apart on a sofa" style="background:linear-gradient(135deg,#6a5848,#b48a5e 60%,#d9b07a)"></div>
  <div class="news-date">27 April 2020</div>
  <div class="news-title">Lorem Ipsum is simply dummy text</div>
  <div class="news-text">Lorem Ipsum is simply dummy text of the printing and typesetting industry. Lorem Ipsum has been the industry's standard dummy text...</div>
  <div class="news-more">READ MORE</div>
</div>
<div class="abs news-card" style="left:464px">
  <div class="news-photo" role="img" aria-label="Gavel beside paper family cut-outs" style="background:linear-gradient(135deg,#5a3a22,#a0683a 55%,#d8c8b4)"></div>
  <div class="news-date">27 April 2020</div>
  <div class="news-title">Lorem Ipsum is simply dummy text</div>
  <div class="news-text">Lorem Ipsum is simply dummy text of the printing and typesetting industry. Lorem Ipsum has been the industry's standard dummy text...</div>
  <div class="news-more">READ MORE</div>
</div>
<div class="abs news-card" style="left:768px">
  <div class="news-photo" role="img" aria-label="Statue of justice against the sky" style="background:linear-gradient(135deg,#d9e8e4,#7eb6c8 55%,#2d5f86)"></div>
  <div class="news-date">27 April 2020</div>
  <div class="news-title">Lorem Ipsum is simply dummy text</div>
  <div class="news-text">Lorem Ipsum is simply dummy text of the printing and typesetting industry. Lorem Ipsum has been the industry's standard dummy text...</div>
  <div class="news-more">READ MORE</div>
</div>

<!-- Contact -->
<div class="abs contact"></div>
<h2 class="abs section-title" style="left:0;top:3610px;width:1200px;color:#fff">Contact Us</h2>
<p class="abs contact-sub">To discuss your matter with either Mr. Tallowfield or Mr. Marsh send us your details about your situation or contact us directly at</p>
<div class="abs contact-phone">
  <svg width="42" height="42" viewBox="0 0 42 42" fill="none" stroke="#fff" stroke-width="1.6"><circle cx="21" cy="21" r="19"/><path d="M14 12.5c1-1 2.3-.8 2.9.3l1.7 3c.5.9.2 1.8-.5 2.3l-1 .8c1 2.4 3 4.4 5.4 5.5l.9-1c.6-.7 1.5-.9 2.3-.4l3 1.7c1 .6 1.2 1.9.3 2.9l-1 1.2c-1 1.1-2.7 1.5-4.1.9-4.8-2-8.6-5.8-10.6-10.6-.6-1.4-.2-3.1.9-4.1z"/></svg>
  (555) 014-2141
</div>
<div class="abs field" style="left:161px;top:3800px;width:204px">First Name</div>
<div class="abs field" style="left:378px;top:3800px;width:203px">Last Name</div>
<div class="abs field" style="left:161px;top:3853px;width:204px">Email</div>
<div class="abs field" style="left:378px;top:3853px;width:203px">Phone</div>
<div class="abs field" style="left:161px;top:3905px;width:420px">Practice Areas</div>
<div class="abs field" style="left:161px;top:3958px;width:420px;height:82px">Massage</div>
<div class="abs btn send-btn">Send Massage</div>
<div class="abs map" role="img" aria-label="Street map showing the office location in Fenmoor"></div>

<!-- Footer -->
<div class="abs footer"></div>
<div class="abs f-icon" style="left:161px">
  <svg width="18" height="22" viewBox="0 0 18 22" fill="#fff"><path d="M9 0C4 0 0 4 0 9c0 6.5 9 13 9 13s9-6.5 9-13c0-5-4-9-9-9zm0 12.5A3.5 3.5 0 1 1 9 5.5a3.5 3.5 0 0 1 0 7z"/></svg>
</div>
<div class="abs" style="left:237px;top:4228px">
  <div class="f-label">ADDRESS</div>
  <div class="f-value">48 Civic Plaza Drive Suite 210<br>Fenmoor, NJ 07999</div>
</div>
<div class="abs f-icon" style="left:465px">
  <svg width="22" height="22" viewBox="0 0 24 24" fill="#fff"><path d="M6.6 10.8c1.4 2.8 3.8 5.1 6.6 6.6l2.2-2.2c.3-.3.7-.4 1-.2 1.1.4 2.3.6 3.6.6.6 0 1 .4 1 1V20c0 .6-.4 1-1 1C10.6 21 3 13.4 3 4c0-.6.4-1 1-1h3.5c.6 0 1 .4 1 1 0 1.3.2 2.5.6 3.6.1.3 0 .7-.2 1l-2.3 2.2z"/></svg>
</div>
<div class="abs" style="left:540px;top:4228px">
  <div class="f-label">CALL US</div>
  <div class="f-value" style="font-size:13px">(555) 014-2141</div>
</div>
<div class="abs f-icon" style="left:770px">
  <svg width="22" height="20" viewBox="0 0 22 20" fill="none" stroke="#fff" stroke-width="1.8"><rect x="5" y="1" width="12" height="6"/><rect x="1" y="7" width="20" height="9" rx="1.5"/><rect x="5" y="12" width="12" height="7" fill="#2e2f33"/></svg>
</div>
<div class="abs" style="left:845px;top:4228px">
  <div class="f-label">FAX</div>
  <div class="f-value">(555) 014-1257</div>
</div>
<div class="abs copyright">© <span>TALLOWFIELD | MARSH</span> - 2020. All Right Reserved.</div>

</body>
</html>
```